Surfing fin design company

Design and build a website.Technical scope - SEO optimisation for high impact results. Website will have high quality videos and images but will be quick to download and transition from one page to the next. It will have a selling function with product of the month(advertised on landing page), shop, rotating/zoom images, selection, basket (discount voucher, postage functions) and pay functionality. Functioning membership area with blog, and database for recording all data.... Automatic email function upon; prolonged use time on site, submission of personal data, purchase and drop shipping (variables controlled by admin privileges)Landing page will multiple designs and formats (for future optimisation), scrolling points of interest from different parts of the sites.Style - The website will have an initial landing page with a modern cool surfing vibe/theme but appeal to both surf groms and commercial surf companies. Abstract stock wave images and videosWant to have low/basic technical Admin interface to manage membership, email and content.

Coding

Coded - Design and coding required

Number of Pages Required

5+ page

Colors

Designer to choose colors to be used in the design.

Requirements
Must have
• Must include the company logo attached

```html
<!DOCTYPE html>
<html lang="en">
<head>
<meta charset="utf-8">
<title>Keelwave – Surf Fins</title>
<link href="https://fonts.googleapis.com/css2?family=Lato:wght@400;700;900&display=swap" rel="stylesheet">
<style>
:root{
  --blue:#2b8fd6;
  --blue-dark:#1a6fb4;
  --blue-deep:#0f4f8f;
  --ink:#1c1c1c;
  --text:#555;
  --grey-bg:#f2f3f5;
  --white:#fff;
  --line:#9ccbee;
}
*{margin:0;padding:0;box-sizing:border-box}
html,body{width:1200px;height:3543px;overflow:hidden}
body{position:relative;background:var(--white);font-family:'Lato',sans-serif;color:var(--ink)}
.abs{position:absolute}
a{color:inherit;text-decoration:none}

/* header */
.brand{font-family:'Lato',sans-serif;font-weight:900;color:var(--blue);display:flex;align-items:center;gap:10px}
.brand .dot{width:18px;height:18px;border-radius:50%;background:var(--blue)}
.header-brand{left:76px;top:34px;font-size:44px}
.search{left:531px;top:40px;width:383px;height:36px;border:1px solid #bbb;border-radius:18px;display:flex;align-items:center;padding-left:16px;font-size:13px;color:#777;overflow:hidden}
.search .btn{position:absolute;right:0;top:0;width:50px;height:100%;background:var(--ink);border-radius:0 18px 18px 0;display:flex;align-items:center;justify-content:center}
.account-links{left:936px;top:48px;font-size:14px;color:#555}
.nav{left:76px;top:111px;width:1048px;height:57px;background:var(--blue);border-radius:28px;box-shadow:0 4px 10px rgba(0,0,0,.15);display:flex;align-items:center;padding:0 30px;color:var(--white);font-size:15px;font-weight:700}
.nav ul{list-style:none;display:flex;gap:44px}
.nav .cart{margin-left:auto;display:flex;align-items:center;gap:10px}

/* hero */
.hero{left:0;top:137px;width:1200px;height:570px;background:linear-gradient(160deg,#6aa7c9 0%,#c9d3d6 35%,#e7a24e 55%,#2a78b8 75%,#8fa3ad 100%)}
.hero-title{left:0;top:312px;width:1200px;text-align:center;color:var(--white);font-size:74px;font-weight:900;text-shadow:0 2px 8px rgba(0,0,0,.25)}
.hero-sub{left:0;top:396px;width:1200px;text-align:center;color:var(--white);font-size:24px;font-weight:700}
.hero-btn{left:496px;top:449px;width:208px;height:54px;background:#111;color:var(--white);border-radius:27px;font-size:24px;font-weight:700;display:flex;align-items:center;justify-content:center}

/* intro */
.section-title{font-size:38px;font-weight:700;color:var(--ink)}
.intro-title{left:0;top:752px;width:1200px;text-align:center}
.intro-text{left:100px;top:815px;width:1000px;text-align:center;font-size:14px;line-height:34px;color:var(--text)}

/* products */
.products-bg{left:0;top:960px;width:1200px;height:600px}
.products-title{left:0;top:1080px;width:1200px;text-align:center;color:var(--white);font-size:36px;font-weight:700}
.card{top:1157px;width:238px;height:298px;background:var(--white);border-radius:10px;box-shadow:0 4px 12px rgba(0,0,0,.15)}
.card .photo{position:absolute;left:35px;top:18px;width:168px;height:140px;border-radius:6px}
.card .name{position:absolute;top:168px;width:100%;text-align:center;color:var(--blue);font-size:18px;font-weight:700}
.card .desc{position:absolute;top:194px;left:20px;right:20px;text-align:center;font-size:14px;line-height:20px;color:#444}
.card .price{position:absolute;left:18px;top:254px;font-size:22px;font-weight:700}
.card .icons{position:absolute;right:18px;top:254px;display:flex;gap:8px}
.card .icons span{width:28px;height:28px;border:1.5px solid #555;border-radius:50%;display:flex;align-items:center;justify-content:center;font-size:13px;font-weight:900;color:#333}

/* product of month */
.pom-title{left:76px;top:1633px}
.pom-text{left:76px;top:1692px;width:600px;font-size:14px;line-height:30px;color:var(--text)}
.pom-price{left:76px;top:1820px;font-size:66px;font-weight:700;color:var(--blue)}
.pom-price sup{font-size:36px;vertical-align:top;position:relative;top:10px}
.pom-btn{left:76px;top:1920px;width:205px;height:50px;background:var(--blue);color:var(--white);border-radius:25px;font-size:22px;font-weight:700;display:flex;align-items:center;justify-content:center}
.pom-art{left:700px;top:1655px;width:430px;height:330px;background:radial-gradient(ellipse at 50% 45%,#2a4d93 0%,#3b6fb6 45%,#cfe4f4 70%,#fff 90%);border-radius:8px}

/* blog */
.grey-band{left:0;top:2000px;width:1200px;height:1260px;background:var(--grey-bg)}
.blog-title{left:76px;top:2135px}
.post{top:2204px;width:330px}
.post .photo{width:330px;height:177px;border-radius:8px}
.post h3{margin-top:22px;font-size:22px;line-height:31px;font-weight:700}
.post .more{display:block;margin-top:10px;font-size:15px;font-weight:700;color:var(--blue)}
.play{position:absolute;left:145px;top:70px;width:40px;height:40px;border-radius:50%;background:rgba(255,255,255,.9)}

/* membership */
.member{left:76px;top:2563px;width:1048px;height:160px;background:#111;border-radius:8px}
.member h2{position:absolute;left:94px;top:56px;font-size:36px;font-weight:400;color:var(--white)}
.member .input{position:absolute;left:399px;top:56px;width:340px;height:50px;background:var(--white);border-radius:25px;font-size:14px;color:#555;display:flex;align-items:center;padding-left:20px}
.member .join{position:absolute;left:751px;top:56px;width:200px;height:50px;background:var(--blue);border-radius:25px;color:var(--white);font-size:18px;font-weight:700;display:flex;align-items:center;justify-content:center}

/* contact */
.offer{left:76px;top:2780px;width:328px;height:366px;border-radius:8px;overflow:hidden;background:linear-gradient(180deg,#2a8fd6 0%,#1d78c1 55%,#c63043 80%,#e7b39a 100%)}
.offer-text{left:76px;top:2828px;width:328px;text-align:center;color:var(--white);font-weight:700}
.offer-text .l1{font-size:36px}
.offer-text .l2{font-size:60px;line-height:64px;font-weight:900}
.offer-text .l2 small{font-size:34px;font-weight:700}
.contact-title{left:432px;top:2768px}
.field{height:48px;border:1.5px solid var(--line);border-radius:24px;font-size:14px;color:#333;padding:14px 22px;background:var(--white)}
.message{left:432px;top:2971px;width:692px;height:110px;border-radius:14px}
.submit{left:435px;top:3097px;width:203px;height:50px;background:#111;color:var(--white);border-radius:25px;font-size:24px;font-weight:700;display:flex;align-items:center;justify-content:center}

/* footer */
.footer-brand{left:76px;top:3318px;font-size:40px}
.copyright{left:76px;top:3404px;font-size:13px;line-height:26px;color:#333}
.social{left:76px;top:3468px;display:flex;gap:18px}
.social span{width:18px;height:18px;border-radius:50%;background:#444}
.fcol h4{font-size:14px;font-weight:700;color:var(--blue);letter-spacing:.5px;margin-bottom:8px}
.fcol ul{list-style:none;font-size:14px;line-height:28px;color:#333}
.site-map ul{columns:2;column-gap:40px;width:200px}
.news p{font-size:14px;line-height:24px;color:#333;width:220px}
.news .input{margin-top:10px;width:218px;height:32px;border:1.5px solid var(--blue);border-radius:16px;font-size:12px;padding:7px 14px;color:#333;position:relative}
.pay{left:909px;top:3470px;display:flex;gap:9px}
.pay span{width:34px;height:22px;border-radius:3px;background:#8a8f96}
</style>
</head>
<body>

<!-- header -->
<div class="abs brand header-brand"><span class="dot"></span>Keelwave</div>
<div class="abs search">Search...
  <span class="btn"><svg width="18" height="18" viewBox="0 0 20 20"><circle cx="8" cy="8" r="6" stroke="#fff" stroke-width="2.5" fill="none"/><line x1="12.5" y1="12.5" x2="18" y2="18" stroke="#fff" stroke-width="2.5"/></svg></span>
</div>
<div class="abs account-links">Log In &nbsp;|&nbsp; Register &nbsp;|&nbsp; Wishlist</div>

<div class="hero abs" role="img" aria-label="Photo of colourful surf fins lined up on a surfboard"></div>
<svg class="abs" style="left:0;top:610px" width="1200" height="100" viewBox="0 0 1200 100">
  <path d="M0 92 Q300 30 650 50 T1200 20 L1200 100 L0 100 Z" fill="#fff"/>
  <path d="M0 86 Q300 24 650 44 T1200 14" stroke="var(--blue)" stroke-width="6" fill="none"/>
</svg>

<nav class="abs nav">
  <ul><li>Home</li><li>About Us</li><li>Products</li><li>Membership</li><li>Blog</li><li>Shop</li><li>Contact Us</li></ul>
  <span class="cart"><svg width="18" height="16" viewBox="0 0 18 16"><path d="M0 1h3l2 9h10l2-7H4" stroke="#fff" stroke-width="2" fill="none"/><circle cx="7" cy="14" r="1.6" fill="#fff"/><circle cx="14" cy="14" r="1.6" fill="#fff"/></svg>My Cart (0)</span>
</nav>

<h1 class="abs hero-title">WELCOME TO KEELWAVE</h1>
<p class="abs hero-sub">Donec ligula risus, euismod et maximus sed, blandit ut ipsum</p>
<a class="abs hero-btn">Shop Now</a>

<!-- intro -->
<h2 class="abs section-title intro-title">Welcome to Keelwave</h2>
<p class="abs intro-text">Cras lorem magna, vestibulum id facilisis in, dapibus vel arcu. Cras rhoncus nunc vel urna dictum tristique. In velit leo, hendrerit non pellentesque a, tincidunt eget enim. Nulla pretium ornare orci nec porttitor. Donec vitae elit rutrum, sodales elit id, pretium risus. Sed varius pharetra urna ut pretium. Sed ultricies tellus sed nisi ultricies tincidunt. Nulla iaculis nisl vel odio elementum, non maximus eros mattis</p>

<!-- products -->
<svg class="abs products-bg" viewBox="0 0 1200 600" preserveAspectRatio="none">
  <defs><linearGradient id="sea" x1="0" y1="0" x2="0" y2="1"><stop offset="0" stop-color="#2b8fd6"/><stop offset=".7" stop-color="#1d74bd"/><stop offset="1" stop-color="#0f4f8f"/></linearGradient></defs>
  <path d="M0 40 Q300 -10 620 30 T1200 20 L1200 540 Q900 600 600 560 T0 570 Z" fill="url(#sea)"/>
</svg>
<h2 class="abs products-title">List of Product</h2>

<div class="abs card" style="left:76px"><div class="photo" role="img" aria-label="Blue surf fin" style="background:linear-gradient(160deg,#6fb6e8,#1f79c4)"></div><div class="name">Product Name</div><div class="desc">Cras rhoncus nunc vel urna dictum tristique.</div><div class="price">$10.00</div><div class="icons"><span>⛟</span><span>♥</span><span>i</span></div></div>
<div class="abs card" style="left:347px"><div class="photo" role="img" aria-label="Black surf fin" style="background:linear-gradient(160deg,#555,#111)"></div><div class="name">Product Name</div><div class="desc">Cras rhoncus nunc vel urna dictum tristique.</div><div class="price">$10.00</div><div class="icons"><span>⛟</span><span>♥</span><span>i</span></div></div>
<div class="abs card" style="left:617px"><div class="photo" role="img" aria-label="Red surf fin" style="background:linear-gradient(160deg,#f06a6a,#c8182a)"></div><div class="name">Product Name</div><div class="desc">Cras rhoncus nunc vel urna dictum tristique.</div><div class="price">$10.00</div><div class="icons"><span>⛟</span><span>♥</span><span>i</span></div></div>
<div class="abs card" style="left:888px"><div class="photo" role="img" aria-label="Turquoise surf fin" style="background:linear-gradient(160deg,#4fc0e8,#1760a8)"></div><div class="name">Product Name</div><div class="desc">Cras rhoncus nunc vel urna dictum tristique.</div><div class="price">$10.00</div><div class="icons"><span>⛟</span><span>♥</span><span>i</span></div></div>

<!-- product of the month -->
<div class="grey-band abs"></div>
<svg class="abs" style="left:0;top:1560px" width="1200" height="500" viewBox="0 0 1200 500">
  <path d="M0 0 H1200 V440 Q900 520 600 460 T0 470 Z" fill="#fff"/>
  <path d="M0 468 Q300 430 600 458 T1200 438" stroke="var(--blue)" stroke-width="6" fill="none"/>
</svg>
<h2 class="abs section-title pom-title">Product of the Month</h2>
<p class="abs pom-text">Cras lorem magna, vestibulum id facilisis in, dapibus vel arcu. Cras rhoncus nunc vel urna dictum tristique. In velit leo, hendrerit non pellentesque a, &nbsp;tincidunt eget enim. Nulla pretium ornare orci nec porttitor. Donec vitae elit rutrum, sodales elit id, pretium risus. Sed varius pharetra urna ut pretium.</p>
<div class="abs pom-price"><sup>$</sup>12.00</div>
<a class="abs pom-btn">Buy Now</a>
<div class="abs pom-art" role="img" aria-label="Illustrated navy surf fin with hand-lettered surf slogan and water splash"></div>

<!-- blog -->
<h2 class="abs section-title blog-title">Blog Posts</h2>
<article class="abs post" style="left:76px"><div class="photo" role="img" aria-label="Video still of red fins on a board by the sea" style="background:linear-gradient(180deg,#8fa4b4,#c63a3a 60%,#7c8790);position:relative"><span class="play"></span></div><h3>Vestibulum cursus a turpis quis facilisis euismod vitae..</h3><a class="more">Read More</a></article>
<article class="abs post" style="left:432px"><div class="photo" role="img" aria-label="Photo of black and red fins on a beach" style="background:linear-gradient(180deg,#6a7d8c,#c89a55 55%,#3d5f86)"></div><h3>Vestibulum cursus a turpis quis facilisis euismod vitae..</h3><a class="more">Read More</a></article>
<article class="abs post" style="left:794px"><div class="photo" role="img" aria-label="Video still of fins in a surf shop" style="background:linear-gradient(180deg,#4d5d6c,#b54b7a 55%,#2a2a33);position:relative"><span class="play"></span></div><h3>Vestibulum cursus a turpis quis facilisis euismod vitae..</h3><a class="more">Read More</a></article>

<!-- membership -->
<section class="abs member">
  <h2>Join Membership</h2>
  <div class="input">Email Address</div>
  <a class="join">Join Now</a>
</section>

<!-- contact -->
<div class="abs offer" role="img" aria-label="Hand holding a red discount card"></div>
<div class="abs offer-text"><div class="l1">Get Flat</div><div class="l2">20% <small>Off</small></div></div>
<h2 class="abs section-title contact-title">Contact Form</h2>
<div class="abs field" style="left:432px;top:2837px;width:338px">Name</div>
<div class="abs field" style="left:786px;top:2837px;width:338px">Email Address</div>
<div class="abs field" style="left:432px;top:2905px;width:338px">Phone No</div>
<div class="abs field" style="left:786px;top:2905px;width:338px">Product Type</div>
<div class="abs field message">Message</div>
<a class="abs submit">Submit</a>

<svg class="abs" style="left:0;top:3180px" width="1200" height="90" viewBox="0 0 1200 90">
  <path d="M0 30 Q300 80 650 68 T1200 50 V90 H0 Z" fill="#fff"/>
  <path d="M0 30 Q300 80 650 68 T1200 50" stroke="var(--blue)" stroke-width="6" fill="none"/>
</svg>

<!-- footer -->
<div class="abs brand footer-brand"><span class="dot"></span>Keelwave</div>
<p class="abs copyright">Copyright © 2019 - Company Name<br>All Right Reserved</p>
<div class="abs social"><span></span><span></span><span></span><span></span><span></span></div>

<div class="abs fcol site-map" style="left:342px;top:3310px"><h4>SITE MAP</h4><ul><li>Home</li><li>About Us</li><li>Products</li><li>Membership</li><li>Blog</li><li>Shop</li><li>Contact Us</li></ul></div>
<div class="abs fcol" style="left:565px;top:3310px"><h4>PRODUCT</h4><ul><li>Curabitur</li><li>Pellentesque risus</li><li>Duiquis</li><li>Placerat</li></ul></div>
<div class="abs fcol" style="left:732px;top:3310px"><h4>MY ACCOUNT</h4><ul><li>Curabitur</li><li>Pellentesque risus</li><li>Duiquis</li><li>Placerat</li></ul></div>
<div class="abs fcol news" style="left:905px;top:3310px"><h4>NEWSLETTER</h4><p>Curabitur pellentesque risus dui, quis placerat</p>
  <div class="input">Enter Email Address<svg style="position:absolute;right:10px;top:9px" width="10" height="12" viewBox="0 0 10 12"><path d="M2 1l6 5-6 5" stroke="#333" stroke-width="2" fill="none"/></svg></div>
</div>
<div class="abs pay"><span></span><span></span><span></span><span></span><span></span></div>

</body>
</html>
```